Marlowe Ridge Holdings

I have a real estate investment business.

** I need editable vector files of the final design.

Industry/Entity Type

Real Estate

Contact Information for Business Card

I would like the card to be clear and direct with the company name and contact info. I would prefer not to have a design that is too busy (i.e., with excessive detail) in the business card.

Font styles to use
Sans Serif

Requirements
Must have
• My card must have the following information listed below:
• Company name: Marlowe Ridge Holdings LLC
• My name: Daniel Vestrap
• Phone number: (555) 218-9064
• Email address: dlvestrap@fernmail.example
• Keywords: “Real Estate Investments”
Nice to have
• I would like to have a design that resembles the characteristics/uses of obsidian stone which resembles something related to strength and resilience. Perhaps something with sharp, sleek color transitions as well.

```html
<!DOCTYPE html>
<html lang="en">
<head>
<meta charset="utf-8">
<title>Marlowe Ridge Holdings – Business Card</title>
<link rel="stylesheet" href="https://fonts.googleapis.com/css2?family=Montserrat:wght@600;700&family=Lato:wght@400&display=swap">
<style>
  :root {
    --backdrop: #3a302c;
    --card-white: #fbfbfb;
    --navy: #1f2279;
    --stone-grey: #7b7b7b;
    --text-grey: #8a8a8a;
    --rule-grey: #c4c4c4;
    --contact-grey: #6b6b6b;
  }
  * { margin: 0; padding: 0; box-sizing: border-box; }
  html, body {
    width: 1200px; height: 844px; overflow: hidden;
    background: var(--backdrop);
  }
  .canvas {
    position: relative; width: 1200px; height: 844px;
  }
  .card {
    position: absolute; width: 500px; height: 286px;
    border-radius: 2px;
    box-shadow: 0 10px 24px rgba(0,0,0,0.35);
    overflow: hidden;
  }
  /* Front */
  .card-front {
    left: 70px; top: 300px;
    background: var(--card-white);
  }
  .brand {
    position: absolute; left: 230px; top: 46px; width: 230px;
    text-align: center;
  }
  .brand-row {
    display: flex; align-items: center; justify-content: center; gap: 10px;
  }
  .brand-dot {
    width: 22px; height: 22px; border-radius: 50%;
    background: var(--navy); flex: none;
  }
  .brand-name {
    font-family: "Montserrat", sans-serif; font-weight: 700;
    font-size: 15px; letter-spacing: 0.5px; color: var(--navy);
    text-transform: uppercase; line-height: 1.15; text-align: left;
  }
  .brand-rule {
    height: 1px; background: var(--rule-grey); margin: 12px 6px 8px;
  }
  .tagline {
    font-family: "Lato", sans-serif; font-size: 13px;
    letter-spacing: 0.6px; color: var(--text-grey); text-transform: uppercase;
  }
  .holder {
    position: absolute; left: 38px; bottom: 34px;
  }
  .holder-name {
    font-family: "Montserrat", sans-serif; font-weight: 600;
    font-size: 17px; color: var(--navy); text-transform: uppercase;
    margin-bottom: 12px;
  }
  .contact {
    display: flex; align-items: center; gap: 6px;
    font-family: "Lato", sans-serif; font-size: 14px; color: var(--contact-grey);
    line-height: 1.5;
  }
  .contact svg { width: 12px; height: 12px; fill: var(--navy); flex: none; }
  /* Back */
  .card-back {
    left: 630px; top: 260px;
    background: linear-gradient(90deg, var(--stone-grey) 0 40%, var(--navy) 40% 100%);
  }
  .back-mark {
    position: absolute; left: 120px; top: 63px;
    width: 160px; height: 160px; border-radius: 50%;
    background: var(--card-white);
    display: flex; align-items: center; justify-content: center;
  }
  .back-name {
    position: absolute; left: 300px; top: 113px; width: 180px;
    font-family: "Montserrat", sans-serif; font-weight: 700;
    font-size: 18px; line-height: 1.25; color: var(--card-white);
    text-transform: uppercase;
  }
</style>
</head>
<body>
<main class="canvas">
  <section class="card card-front">
    <div class="brand">
      <div class="brand-row">
        <span class="brand-dot"></span>
        <span class="brand-name">Marlowe Ridge Holdings</span>
      </div>
      <div class="brand-rule"></div>
      <p class="tagline">Real Estate Investments</p>
    </div>
    <div class="holder">
      <p class="holder-name">Daniel Vestrap</p>
      <p class="contact">
        <svg viewBox="0 0 24 24" aria-hidden="true"><path d="M6.6 10.8a15.1 15.1 0 0 0 6.6 6.6l2.2-2.2a1 1 0 0 1 1-.25 11.4 11.4 0 0 0 3.6.57 1 1 0 0 1 1 1V20a1 1 0 0 1-1 1A17 17 0 0 1 3 4a1 1 0 0 1 1-1h3.5a1 1 0 0 1 1 1c0 1.25.2 2.45.57 3.57a1 1 0 0 1-.25 1z"/></svg>
        (555) 218-9064
      </p>
      <p class="contact">
        <svg viewBox="0 0 24 24" aria-hidden="true"><path d="M2 5h20v14H2zm2 2v.5l8 5 8-5V7l-8 5z"/></svg>
        dlvestrap@fernmail.example
      </p>
    </div>
  </section>

  <section class="card card-back">
    <div class="back-mark"></div>
    <p class="back-name">Marlowe Ridge Holdings</p>
  </section>
</main>
</body>
</html>
```